BRIVON - Business Card Design Project

We need a business card design for a consultant company called BRIVON, LLC. (stands for Bright Retail Inventory Venture Operations Network). The company provides Information Technology solutions, custom applications, services for financial and supply chain worldwide and focuses on business IT process improvements and all the steps leading to the procurement or integrating of any Enterprise related systems.

Industry/Entity Type

Financial

Requirements
Must have
• - In the submitted proposed version you should have one variant with black background and one with white.
The designer should show the shadow element of the company name in binary code (010000100101001001001001010101100100111101001110). It can be in one line or split in two

In your example please use the following info
Peter Dorne
Principal Consultant
pdorne@brivonhq.net
+1 (555) 014 - 2298

Please keep in mind that the design should have some spaces to add the second phone and/or web site name
Nice to have
• Since this IT company and is working closely with Accounting and Logistics Application you can add some elements (contour only) of these types of the bussines as well (for example some $ or euro sign or truck or warehouse element)
Should not have
• Don’t use any extra color that is not in the company color logo pattern

```html
<!DOCTYPE html>
<html lang="en">
<head>
<meta charset="utf-8">
<title>BRIVON Business Cards</title>
<link rel="stylesheet" href="https://fonts.googleapis.com/css2?family=Roboto:wght@300;400;700&family=Roboto+Mono:wght@400&display=swap">
<style>
  :root {
    --page-bg: #e9e6e1;
    --card-light: #ffffff;
    --card-dark: #141414;
    --ink-dark: #1e1e1e;
    --ink-mid: #444444;
    --ink-soft: #9a9a9a;
    --ink-light: #f2f2f2;
    --ink-light-mid: #c9c9c9;
    --ink-light-soft: #6e6e6e;
    --band-black: #111111;
    --band-white: #f4f4f4;
    --brand-blue: #2f6fb0;
    --brand-orange: #f0a21c;
    --brand-green: #5aa33a;
  }
  * { box-sizing: border-box; margin: 0; padding: 0; }
  html, body {
    width: 1200px; height: 1024px; overflow: hidden;
    background: var(--page-bg);
    font-family: "Roboto", Arial, sans-serif;
  }
  .card-set {
    position: absolute; left: 215px; top: 48px;
    display: flex; flex-direction: column; gap: 48px;
  }
  .card {
    position: relative;
    width: 770px; height: 440px;
    background: var(--card-light);
    box-shadow: 0 8px 26px rgba(0,0,0,0.18);
    overflow: hidden;
    color: var(--ink-dark);
  }
  .card__decor {
    position: absolute; right: 0; top: 0;
    width: 410px; height: 280px;
    background: radial-gradient(ellipse at 65% 30%, rgba(200,205,210,0.45), rgba(255,255,255,0) 65%);
  }
  .brand {
    position: absolute; left: 66px; top: 110px;
    display: flex; align-items: center; gap: 25px;
  }
  .brand__dot {
    width: 70px; height: 70px; border-radius: 50%;
    background: var(--brand-blue);
  }
  .brand__name {
    font-size: 88px; font-weight: 400; letter-spacing: 7px;
    line-height: 1;
  }
  .binary {
    position: absolute; left: 161px; top: 207px;
    font-family: "Roboto Mono", monospace; font-size: 10px;
    letter-spacing: 0.45px; color: var(--ink-soft);
  }
  .person {
    position: absolute; left: 66px; top: 253px;
    white-space: nowrap;
  }
  .person__name {
    font-size: 26px; font-weight: 700; text-transform: uppercase;
  }
  .person__role {
    font-size: 17px; font-weight: 300; margin-left: 8px; color: var(--ink-mid);
  }
  .contact {
    position: absolute; left: 66px; top: 297px;
    font-size: 17.5px; font-weight: 300; color: var(--ink-mid); line-height: 29px;
    white-space: nowrap;
  }
  .contact__key { font-weight: 700; margin-right: 6px; }
  .contact__key--p { color: var(--brand-blue); }
  .contact__key--e { color: var(--brand-orange); }
  .contact__key--w { color: var(--brand-green); margin-left: 14px; }
  .contact__sep { margin: 0 9px; color: var(--ink-soft); }
  .band {
    position: absolute; left: 0; bottom: 0; width: 100%; height: 32px;
    display: flex;
  }
  .band__base { flex: 0 0 64%; background: var(--band-black); }
  .band__blue { flex: 1; background: var(--brand-blue); }
  .band__orange { flex: 1; background: var(--brand-orange); }
  .band__green { flex: 1; background: var(--brand-green); }

  .card--dark { background: var(--card-dark); color: var(--ink-light); }
  .card--dark .card__decor {
    background: radial-gradient(ellipse at 65% 30%, rgba(90,95,100,0.35), rgba(20,20,20,0) 65%);
  }
  .card--dark .binary { color: var(--ink-light-soft); }
  .card--dark .person__role,
  .card--dark .contact { color: var(--ink-light-mid); }
  .card--dark .contact__sep { color: var(--ink-light-soft); }
  .card--dark .band__base { background: var(--band-white); }
</style>
</head>
<body>
  <div class="card-set">
    <div class="card card--light">
      <div class="card__decor" role="img" aria-label="Faint flowing line-art pattern in light grey"></div>
      <div class="brand">
        <span class="brand__dot"></span>
        <span class="brand__name">BRIVON</span>
      </div>
      <div class="binary">010000100101001001001001010101100100111101001110</div>
      <div class="person">
        <span class="person__name">Peter Dorne</span>
        <span class="person__role">Principal Consultant</span>
      </div>
      <div class="contact">
        <div>
          <span class="contact__key contact__key--p">p :</span>+1 (555) 014 - 2298
          <span class="contact__sep">|</span>+1 (555) 014 - 7731
        </div>
        <div>
          <span class="contact__key contact__key--e">e :</span>pdorne@brivonhq.net
          <span class="contact__key contact__key--w">w :</span>www.brivonhq.net
        </div>
      </div>
      <div class="band">
        <div class="band__base"></div>
        <div class="band__blue"></div>
        <div class="band__orange"></div>
        <div class="band__green"></div>
      </div>
    </div>

    <div class="card card--dark">
      <div class="card__decor" role="img" aria-label="Faint flowing line-art pattern in dark grey"></div>
      <div class="brand">
        <span class="brand__dot"></span>
        <span class="brand__name">BRIVON</span>
      </div>
      <div class="binary">010000100101001001001001010101100100111101001110</div>
      <div class="person">
        <span class="person__name">Peter Dorne</span>
        <span class="person__role">Principal Consultant</span>
      </div>
      <div class="contact">
        <div>
          <span class="contact__key contact__key--p">p :</span>+1 (555) 014 - 2298
          <span class="contact__sep">|</span>+1 (555) 014 - 7731
        </div>
        <div>
          <span class="contact__key contact__key--e">e :</span>pdorne@brivonhq.net
          <span class="contact__key contact__key--w">w :</span>www.brivonhq.net
        </div>
      </div>
      <div class="band">
        <div class="band__base"></div>
        <div class="band__blue"></div>
        <div class="band__orange"></div>
        <div class="band__green"></div>
      </div>
    </div>
  </div>
</body>
</html>
```